Verimont Designs business card

Front of card should be logo and back of card should be communication info.
Please note: reverse the logo color. Card should be black and everything else white.

Industry/Entity Type

Custom home design/construction

Contact Information for Business Card

Verimont Designs, LLC 614-382-9017 verimontdesigns@quillmail.example

Requirements
Must have
• Square card, Logo on front, communication info on back and perhaps a mini version of the logo on back also. Black card/white lettering. Double sides square card.
Nice to have
• I want to keep it simple. Our product (custom homes) speak for themselves.

```html
<!DOCTYPE html>
<html lang="en">
<head>
<meta charset="utf-8">
<title>Verimont Designs – Business Card</title>
<link rel="stylesheet" href="https://fonts.googleapis.com/css2?family=Outfit:wght@300;400;600;700&display=swap">
<style>
  :root {
    --page: #efeeeb;
    --card: #000000;
    --ink: #ffffff;
    --art: #1a1a1a;
  }
  * { margin: 0; padding: 0; box-sizing: border-box; }
  html, body {
    width: 1200px; height: 1200px; overflow: hidden;
    background: var(--page);
    font-family: "Outfit", Arial, sans-serif;
    color: var(--ink);
  }
  .sheet { position: relative; width: 1200px; height: 1200px; }
  .card {
    position: absolute; left: 322px; width: 551px; height: 551px;
    background: var(--card); border-radius: 38px; overflow: hidden;
  }
  .card--front { top: 34px; }
  .card--back { top: 611px; }

  .house-art {
    position: absolute; background: var(--art); border-radius: 4px;
  }
  .card--front .house-art { left: 105px; top: 117px; width: 346px; height: 243px; }
  .card--back .house-art { left: 400px; top: 296px; width: 160px; height: 260px; }

  .brand { position: absolute; left: 0; right: 0; text-align: center; }
  .card--front .brand { top: 384px; padding-left: 34px; }
  .card--back .brand { top: 162px; padding-left: 10px; }
  .brand__name {
    font-weight: 700; font-size: 42px; line-height: 1; letter-spacing: 0.5px;
    text-transform: uppercase;
  }
  .brand__tagline {
    margin-top: 10px; font-weight: 400; font-size: 20px; line-height: 1;
    letter-spacing: 6.2px; text-transform: uppercase;
  }

  .contacts {
    position: absolute; left: 41px; top: 357px;
    font-size: 20px; line-height: 29px; font-weight: 400;
  }
  .contacts__name { font-weight: 700; }
  .contacts__email { font-size: 18px; }
</style>
</head>
<body>
<main class="sheet">
  <section class="card card--front">
    <div class="house-art" role="img" aria-label="Line illustration of a two-storey custom home with dormers and porch columns"></div>
    <div class="brand">
      <h1 class="brand__name">Verimont Designs</h1>
      <p class="brand__tagline">Custom Home Builders</p>
    </div>
  </section>

  <section class="card card--back">
    <div class="brand">
      <h2 class="brand__name">Verimont Designs</h2>
      <p class="brand__tagline">Custom Home Builders</p>
    </div>
    <div class="contacts">
      <p><span class="contacts__name">Marla Kestrin</span> - CEO</p>
      <p>614-382-9017</p>
      <p><span class="contacts__name">Dov Hallarek</span> - GC</p>
      <p>614-275-8830</p>
      <p class="contacts__email">verimontdesigns@quillmail.example</p>
    </div>
    <div class="house-art" role="img" aria-label="Cropped line illustration of the house's dormer and front door"></div>
  </section>
</main>
</body>
</html>
```